Booking site for apartment in Nice

I have a new design apartment close to the Promenade in central Nice for rental. I would like to make a website to display the apartment through pictures, show availability from a calendar that is updated manually based on bookings and send requests about rental (no online booking).

I would like to have the site sosial media enabled and easy to maintain. I want the site to be responsive. Pictures will be sent later. An estimated number of pictures will be appoximately 20.

Feel free to suggest style, main menu and content elements.

Look for inspiration at bolvista.com.

The request field should contain, name, mobile phone and mail address + the dates (from - to) the want to rent the apartment. I also want Captcha verification as a function for the request.

I got information that the link did not work: Try this: Try http://holvista.com

```html
<!DOCTYPE html>
<html lang="en">
<head>
<meta charset="utf-8">
<title>Azur Loft – Booking Request</title>
<link rel="stylesheet" href="https://fonts.googleapis.com/css2?family=Arimo:wght@400&display=swap">
<style>
  :root {
    --bg-dark: #2a2622;
    --bg-mid: #4a443d;
    --bg-warm: #5e5448;
    --field: #ffffff;
    --placeholder: #7a7a7a;
    --captcha: #b8b8b8;
    --line: #ffffff;
    --accent: #3fb0f2;
    --tab: #8d8a86;
    --icon-faint: #5a5753;
    --thumb: #6a655e;
  }
  * { box-sizing: border-box; margin: 0; padding: 0; }
  html, body { width: 1200px; height: 898px; overflow: hidden; }
  body {
    position: relative;
    font-family: "Arimo", Arial, sans-serif;
    background: var(--bg-dark);
  }
  .room-photo {
    position: absolute; inset: 0;
    background:
      radial-gradient(ellipse at 75% 45%, rgba(120,105,85,.55), transparent 60%),
      linear-gradient(90deg, #3b3a38 0%, #34302c 30%, var(--bg-warm) 60%, #3a332c 100%),
      linear-gradient(180deg, transparent 60%, rgba(0,0,0,.25) 100%);
  }
  .site-mark {
    position: absolute; left: 28px; top: 30px;
    width: 106px; height: 66px;
    display: flex; align-items: center; justify-content: center;
    color: var(--icon-faint); font-size: 18px; letter-spacing: 1px;
    background: rgba(30,28,26,.6);
  }
  .top-icons { position: absolute; left: 150px; top: 48px; display: flex; gap: 14px; }
  .top-icons svg { display: block; }
  .brand {
    position: absolute; left: 783px; top: 375px;
    width: 233px; height: 146px;
    display: flex; align-items: center; justify-content: center; gap: 12px;
    color: #ffffff; font-size: 38px; letter-spacing: 3px;
  }
  .brand-square { width: 12px; height: 12px; background: #ffffff; }
  .gallery { position: absolute; left: 274px; top: 745px; display: flex; gap: 14px; }
  .gallery-thumb { width: 119px; height: 118px; background: var(--thumb); opacity: .75; border: 2px solid rgba(120,115,108,.6); }
  .gallery-thumb:nth-child(1) { background: #7c756c; }
  .gallery-thumb:nth-child(2) { background: #3a3632; }
  .gallery-thumb:nth-child(3) { background: #4a4642; }
  .gallery-thumb:nth-child(4) { background: #5c5955; }
  .gallery-thumb:nth-child(5) { background: #676460; }
  .request-panel {
    position: absolute; left: 16px; top: 17px;
    width: 583px; height: 860px;
    border: 1px solid var(--line);
  }
  .close-btn { position: absolute; left: 557px; top: 9px; color: #fff; font-size: 18px; }
  .field {
    position: absolute; background: var(--field); border: 0;
    font-family: inherit; font-size: 19px; color: var(--placeholder);
    padding: 0 14px; outline: none;
  }
  .field::placeholder { color: var(--placeholder); }
  .field-wide { left: 114px; width: 342px; height: 56px; }
  .field-small { top: 382px; width: 102px; height: 40px; padding: 0; text-align: center; font-size: 19px; }
  .field-message { left: 114px; top: 462px; width: 342px; height: 153px; padding: 10px 11px; resize: none; }
  .consent {
    position: absolute; left: 114px; top: 640px;
    display: flex; align-items: center; gap: 23px;
    color: #fff; font-size: 18px;
  }
  .consent-box { width: 12px; height: 12px; border: 1.5px solid #fff; }
  .captcha-code {
    position: absolute; left: 232px; top: 677px; width: 102px; height: 40px;
    background: var(--field); color: var(--captcha); font-size: 24px;
    display: flex; align-items: center; justify-content: center;
  }
  .send-btn {
    position: absolute; left: 352px; top: 677px; width: 102px; height: 40px;
    background: var(--accent); color: #fff; border: 0;
    font-family: inherit; font-size: 19px;
  }
  .mail-tab {
    position: absolute; left: 0; top: 485px; width: 56px; height: 57px;
    background: var(--tab); display: flex; align-items: center; justify-content: center;
  }
</style>
</head>
<body>
  <div class="room-photo" role="img" aria-label="Dim interior photo of the apartment living room with windows, sofa and TV wall"></div>

  <div class="site-mark">AZUR LOFT</div>
  <div class="top-icons" aria-hidden="true">
    <svg width="26" height="30" viewBox="0 0 26 30"><circle cx="13" cy="10" r="9" fill="#3a6fa0"/><path d="M6 17 L6 29 L13 24 L20 29 L20 17Z" fill="#3a6fa0"/></svg>
    <svg width="28" height="30" viewBox="0 0 28 30"><circle cx="14" cy="15" r="9" fill="none" stroke="var(--icon-faint)" stroke-width="5" stroke-dasharray="4 3"/><circle cx="14" cy="15" r="4" fill="var(--icon-faint)"/></svg>
    <svg width="42" height="30" viewBox="0 0 42 30"><circle cx="10" cy="19" r="8" fill="none" stroke="var(--icon-faint)" stroke-width="3"/><circle cx="32" cy="19" r="8" fill="none" stroke="var(--icon-faint)" stroke-width="3"/><path d="M10 19 L18 8 L28 8 L32 19 M18 8 L21 19 L28 8" fill="none" stroke="var(--icon-faint)" stroke-width="3"/></svg>
  </div>

  <div class="brand"><span class="brand-square"></span>AZUR LOFT</div>

  <div class="gallery">
    <div class="gallery-thumb" role="img" aria-label="Apartment photo: living room"></div>
    <div class="gallery-thumb" role="img" aria-label="Apartment photo: dark bedroom"></div>
    <div class="gallery-thumb" role="img" aria-label="Apartment photo: dining area"></div>
    <div class="gallery-thumb" role="img" aria-label="Apartment photo: bedroom"></div>
    <div class="gallery-thumb" role="img" aria-label="Apartment photo: lounge"></div>
  </div>

  <form class="request-panel">
    <span class="close-btn">X</span>
    <input class="field field-wide" style="top:142px" placeholder="name">
    <input class="field field-wide" style="top:213px" placeholder="phone">
    <input class="field field-wide" style="top:285px" placeholder="e-mail">
    <input class="field field-small" style="left:114px;width:101px" placeholder="check in">
    <input class="field field-small" style="left:234px" placeholder="check out">
    <input class="field field-small" style="left:354px" placeholder="persons">
    <textarea class="field field-message" placeholder="message"></textarea>
    <label class="consent"><span class="consent-box"></span>i agree to recieve commercial data</label>
    <input class="field field-small" style="left:112px;top:677px;width:101px" placeholder="validation">
    <div class="captcha-code">QR09h</div>
    <button class="send-btn" type="button">SEND</button>
  </form>

  <div class="mail-tab" aria-label="Contact">
    <svg width="32" height="20" viewBox="0 0 32 20"><rect x="1" y="1" width="30" height="18" fill="none" stroke="#fff" stroke-width="1.6"/><path d="M1 1 L16 12 L31 1 M1 19 L12 9 M31 19 L20 9" fill="none" stroke="#fff" stroke-width="1.6"/></svg>
  </div>
</body>
</html>
```